Business school needs a web design

Who We are:
KRVT is a small business school that offers programs in Project Management. The school is based in West Africa and welcomes students from the whole area. Our aim is to become one of the reference business schools in Africa.

Project Brief:
The site will include all informations relevant for different types of visitors that we have: actual and future students, companies, mass media, future employees, ect. It will present information about subscription, list of programs, presentation of the school and its team,etc.

What We want:
This competition is for Design only no coding! We need design for two pages.
We did some wireframing for the home page and the list of programs page. We made them just to show how we imagine the website would look like. But we encourage creative designs, so you don't have to stick to the wireframe models.

Sites We like:
http://www.ravenmoorcollege.example/
http://www.belvantis.example/fr/etudes.html
http://www.qtl.example/mba/Pages/default.aspx

Color schemes
The logo of the school is red and black. So the color scheme of the website should match that. For the rest, it is opened to your imagination.
Updates

The payment for the project is now garanteed. Good luck to you all !

Target Market(s)

The target market is diversified because we have students of different ages, also company representatives or employees that might visit the website for recruitment purposes. But the majority of our audience should be aged between 20 - 30 years.

Industry/Entity Type

Small Business

Requirements
Must have
• The design must include two pages: a home page and another interior page : might be the list of programs or any other page relevant to the domain. The Home page must include a slide show at the beginning.
The background page must be white.
Nice to have
• The use of flat design for this project is preferred.
The use of Pelican scaffold as a base for the design is an asset.

```html
<!DOCTYPE html>
<html lang="fr">
<head>
<meta charset="utf-8">
<title>KRVT – Programmes et Formations</title>
<link rel="stylesheet" href="https://fonts.googleapis.com/css2?family=Open+Sans:wght@400;600&family=Arimo:wght@400;700&display=swap">
<style>
:root{
  --brand-red:#a3203f;
  --deep-red:#7d1430;
  --ink:#1a1a1a;
  --text:#444;
  --muted:#777;
  --link:#1f4f8a;
  --header-bg:#f1f1f0;
  --page-bg:#f6f6f6;
  --frame:#d4d4d4;
}
*{box-sizing:border-box;margin:0;padding:0}
html,body{width:1200px;height:1000px;overflow:hidden}
body{position:relative;background:var(--page-bg);font-family:"Arimo",Arial,sans-serif;color:var(--text)}
.topbar{position:absolute;left:0;top:0;width:1200px;height:5px;background:var(--deep-red)}
.site-header{position:absolute;left:0;top:5px;width:1200px;height:130px;background:linear-gradient(#f4f4f3,#ebebea);border-bottom:1px solid #d8d8d8;z-index:2}
.brand{position:absolute;left:88px;top:52px;display:flex;align-items:center;gap:8px;font-family:"Arimo",sans-serif;font-weight:700;font-size:28px;color:var(--ink);letter-spacing:1px}
.brand-mark{width:16px;height:16px;background:var(--brand-red)}
.utility-nav{position:absolute;right:18px;top:16px;display:flex;font-size:12px;color:#666}
.utility-nav span{padding:0 22px;border-left:2px solid var(--brand-red);line-height:12px}
.utility-nav span:first-child{border-left:none}
.main-nav{position:absolute;left:296px;top:68px;display:flex;gap:47px;font-family:"Open Sans",sans-serif;font-size:14.5px;color:#666}
.main-nav .active{color:var(--ink)}
.search{position:absolute;left:1123px;top:61px;width:120px;height:31px;border:1px solid #c8c8c8;border-radius:16px;background:#fff;display:flex;align-items:center;padding-left:10px;gap:8px;font-size:13px;font-style:italic;color:#aaa}
.hero{position:absolute;left:0;top:135px;width:1200px;height:352px;background:
  radial-gradient(ellipse 220px 180px at 760px 230px,#2e4f7a 0%,transparent 70%),
  radial-gradient(ellipse 180px 200px at 470px 260px,#d9b199 0%,transparent 70%),
  linear-gradient(180deg,#8ea36a 0%,#c9c3aa 45%,#b89a84 100%)}
.hero-title{position:absolute;left:90px;top:104px}
.hero-title span{display:inline-block;color:#fff;font-size:29px;line-height:36px;padding:0 9px}
.hero-title .kicker{background:var(--brand-red)}
.hero-title .sub{background:var(--ink);margin-top:2px}
.content{position:absolute;left:60px;top:430px;width:1160px;height:600px;background:#fff;border-top:4px solid var(--deep-red);box-shadow:-3px 0 6px rgba(0,0,0,.08)}
.breadcrumb{position:absolute;left:22px;top:22px;display:flex;align-items:center;gap:10px;font-size:14px;color:var(--muted)}
.breadcrumb a{color:var(--link);text-decoration:none}
.page-title{position:absolute;left:0;width:1160px;top:70px;text-align:center;font-weight:400;font-size:28px;color:#333;padding-right:0}
.page-title b{font-weight:400;color:#222}
.page-title i{display:inline-block;width:8px;height:8px;background:var(--brand-red);margin-right:14px;vertical-align:middle}
.intro{position:absolute;left:0;top:126px;width:1160px;text-align:center;font-size:16px;line-height:29.5px;color:#444;white-space:nowrap;overflow:hidden}
.divider{position:absolute;left:70px;top:281px;width:1060px;height:2px;background:linear-gradient(90deg,transparent,#cfcfcf 20%,#cfcfcf 80%,transparent)}
.program{position:absolute;top:350px;width:322px}
.program h2{font-weight:400;font-size:21px;color:#555;margin-bottom:25px}
.program h2 b{font-weight:400;color:#222}
.program-photo{border:5px solid var(--frame);height:240px;background:linear-gradient(160deg,#d9dcd6 0%,#b9a79c 40%,#c47a9a 75%,#e7d5dc 100%);position:relative}
.program-photo::after{content:"";position:absolute;left:8px;bottom:0;width:46px;height:6px;background:#333}
.program-photo::before{content:"";position:absolute;left:72px;bottom:0;width:226px;height:6px;background:#333}
</style>
</head>
<body>
<div class="topbar"></div>
<header class="site-header">
  <div class="brand"><span class="brand-mark"></span>KRVT</div>
  <nav class="utility-nav"><span>Répertoire du Personel</span><span>Blogue</span><span>Salle de Presse</span><span>Nous Joindre</span></nav>
  <nav class="main-nav"><span class="active">À Propos de l’KRVT</span><span>Programmes Et Formations</span><span>Étudiants</span><span>Nouvelles et Évènements</span><span>Entreprise</span></nav>
  <div class="search"><svg width="16" height="16" viewBox="0 0 16 16"><circle cx="6.5" cy="6.5" r="5" fill="none" stroke="#aaa" stroke-width="2"/><line x1="10" y1="10" x2="15" y2="15" stroke="#aaa" stroke-width="2.5"/></svg>Search</div>
</header>
<section class="hero" role="img" aria-label="Photo floue d’étudiants souriants en plein air">
  <div class="hero-title">
    <span class="kicker">Preparing Students For Tomorrow</span><br>
    <span class="sub">MBA Bussines School</span>
  </div>
</section>
<main class="content">
  <div class="breadcrumb">
    <svg width="14" height="13" viewBox="0 0 14 13"><path d="M7 0L0 6h2v7h4V9h2v4h4V6h2z" fill="#666"/></svg>
    <a href="#">Accueil</a><span>»</span><span>Programmes et Formations</span>
  </div>
  <h1 class="page-title"><i></i>Programmes <b>Et Formations</b></h1>
  <p class="intro">Lorem ipsum dolor sit amet, consectetur adipisicing elit, sed do eiusmod tem et dolore magna aliqua. Ut enim ad minim veniam, quis nostrud exercita tion<br>
  mecos laboris nisi ut aliquip ex ea commodo consequat. Duis aute irure dolor in reprehenderit in voluptate velit esse cillum dolore eu fugiat nulla pariatur.<br>
  Excepteur sint occaecat &nbsp;cupidatat non proident, sunt in culpa qui officia deserunt mollit anim id est laborum.<br>
  &nbsp;Tion ullamco laboris nisi ut aliquip ex ea commodo consequat. Duis aute irure dolor in reprehenderit in voluptate velit esse cillum dolore eu fugiat</p>
  <div class="divider"></div>
  <article class="program" style="left:57px"><h2>Formations <b>Diplomantes</b></h2><div class="program-photo" role="img" aria-label="Photo d’étudiants réunis autour d’une table"></div></article>
  <article class="program" style="left:442px;top:348px"><h2>Certificants <b>Professionnels</b></h2><div class="program-photo" role="img" aria-label="Photo d’étudiants réunis autour d’une table"></div></article>
  <article class="program" style="left:836px"><h2>Formations <b>À La Carte</b></h2><div class="program-photo" role="img" aria-label="Photo d’étudiants réunis autour d’une table"></div></article>
</main>
</body>
</html>
```